Business Card For Quillmoor Financial Consulting

Hi, I would like a business card designed. Bold, modern.
Please use the same design as the logo. I have also attached the website design to see the overall theme.
Wordmark Font
Color: Hex: #01AEF7

```html
<!DOCTYPE html>
<html lang="en">
<head>
<meta charset="UTF-8">
<title>Quillmoor Financial Consulting – Business Card</title>
<link href="https://fonts.googleapis.com/css2?family=Montserrat:wght@700&family=Open+Sans:wght@400;600&display=swap" rel="stylesheet">
<style>
  :root {
    --page-bg: #e9ebee;
    --navy: #0a4569;
    --navy-tint: #1b5679;
    --sky: #2ea3dc;
    --pale-sky: #dbeaf7;
    --white: #ffffff;
    --ink: #1a1a1a;
  }
  * { box-sizing: border-box; margin: 0; padding: 0; }
  html, body { width: 1200px; height: 780px; overflow: hidden; }
  body {
    background: var(--page-bg);
    display: flex;
    align-items: center;
    justify-content: center;
    gap: 40px;
  }
  .card {
    position: relative;
    width: 540px;
    height: 309px;
    overflow: hidden;
    box-shadow: 0 10px 28px rgba(0,0,0,0.18);
  }

  /* Front */
  .card--front { background: var(--navy); }
  .card--front .decor-frame {
    position: absolute;
    left: 150px; top: -30px;
    width: 330px; height: 330px;
    border: 34px solid var(--navy-tint);
  }
  .brand {
    position: absolute;
    left: 70px; top: 112px;
    display: flex;
    align-items: center;
    gap: 16px;
  }
  .brand__square {
    width: 62px; height: 62px;
    border: 7px solid var(--sky);
    flex: none;
  }
  .brand__name {
    font-family: "Montserrat", sans-serif;
    font-weight: 700;
    color: var(--white);
    line-height: 1;
  }
  .brand__name .line-main { display: block; font-size: 46px; letter-spacing: 1px; }
  .brand__name .line-sub  { display: block; font-size: 13px; letter-spacing: 6.2px; margin-top: 8px; }

  /* Back */
  .card--back { background: var(--white); }
  .card--back .decor-frame {
    position: absolute;
    left: 110px; top: 20px;
    width: 300px; height: 300px;
    border: 30px solid var(--pale-sky);
  }
  .person {
    position: absolute;
    left: 40px; top: 128px;
    width: 232px;
    text-align: right;
    font-family: "Open Sans", sans-serif;
  }
  .person__name { color: var(--sky); font-weight: 600; font-size: 27px; line-height: 1.1; }
  .person__role { color: var(--ink); font-size: 14px; margin-top: 2px; }
  .divider {
    position: absolute;
    left: 290px; top: 96px;
    width: 1px; height: 112px;
    background: var(--ink);
  }
  .contact {
    position: absolute;
    left: 310px; top: 112px;
    list-style: none;
    font-family: "Open Sans", sans-serif;
    font-size: 14px;
    color: var(--ink);
  }
  .contact li { display: flex; align-items: center; gap: 8px; height: 26px; }
  .contact svg { width: 15px; height: 15px; flex: none; }
</style>
</head>
<body>

  <section class="card card--front">
    <div class="decor-frame" aria-hidden="true"></div>
    <div class="brand">
      <div class="brand__square" aria-hidden="true"></div>
      <h1 class="brand__name">
        <span class="line-main">QUILLMOOR</span>
        <span class="line-sub">FINANCIAL CONSULTING</span>
      </h1>
    </div>
  </section>

  <section class="card card--back">
    <div class="decor-frame" aria-hidden="true"></div>
    <div class="person">
      <p class="person__name">Mara Lindqvist</p>
      <p class="person__role">Managing Director</p>
    </div>
    <div class="divider" aria-hidden="true"></div>
    <ul class="contact">
      <li>
        <svg viewBox="0 0 24 24" aria-hidden="true"><path fill="#1a1a1a" d="M6.6 10.8a15.2 15.2 0 0 0 6.6 6.6l2.2-2.2a1 1 0 0 1 1-.25 11.4 11.4 0 0 0 3.6.57 1 1 0 0 1 1 1V20a1 1 0 0 1-1 1A17 17 0 0 1 3 4a1 1 0 0 1 1-1h3.5a1 1 0 0 1 1 1c0 1.25.2 2.45.57 3.57a1 1 0 0 1-.25 1z"/></svg>
        (555) 014-2758
      </li>
      <li>
        <svg viewBox="0 0 24 24" aria-hidden="true"><rect x="2" y="5" width="20" height="14" rx="1.5" fill="none" stroke="#1a1a1a" stroke-width="2"/><path d="M3 6l9 7 9-7" fill="none" stroke="#1a1a1a" stroke-width="2"/></svg>
        info@quillmoor.com
      </li>
      <li>
        <svg viewBox="0 0 24 24" aria-hidden="true"><circle cx="12" cy="12" r="9.5" fill="none" stroke="#1a1a1a" stroke-width="2"/><path d="M2.5 12h19M12 2.5c3 3 3 16 0 19M12 2.5c-3 3-3 16 0 19" fill="none" stroke="#1a1a1a" stroke-width="1.6"/></svg>
        www.quillmoor.com
      </li>
    </ul>
  </section>

</body>
</html>
```